Tess Marlowe Communication business card

I am starting a small, country-based business that offers writing, communication and marketing services to a wide range of clients, inner city big business, to mining, through to agriculture.

The appeal of my business is that it's mobile and flexible. It's just me, with lots of hands-on experience on construction and infrastructure projects.

I can provide the following services:

• Communication planning and management
• Issues and media management
• Marketing and communication materials
• Project management and strategy
• Government liaison
• Incident management communication
• Stakeholder management

It would be great to be able to use the elements of the business card design on other stationery.

Industry/Entity Type

Communication

Requirements
Must have
• The following information:

Tess Marlowe
M: 0427 391 864
E: tess@tmcommsmail.com

PO Box 152
Durrandale Q 4472
Nice to have
• a rural element (windmill, workboots, wheat stalk)

```html
<!DOCTYPE html>
<html lang="en">
<head>
<meta charset="utf-8">
<title>Tess Marlowe Communication – Business Card Concepts</title>
<link rel="stylesheet" href="https://fonts.googleapis.com/css2?family=Fira+Sans:wght@400;600&family=Alfa+Slab+One&display=swap">
<style>
  :root{
    --sheet:#ffffff;
    --stage:#8a8a8a;
    --night:#06080f;
    --ocean:#0a5cb3;
    --indigo:#0b1d9e;
    --gold:#e9b526;
    --gold-soft:#f6d458;
    --sky-blue:#3d7df0;
    --yellow-ink:#f2e232;
    --cyan-ink:#5fe0ea;
    --teal-rule:#4fd1c8;
    --red-ink:#c11313;
    --red-rule:#d74a4a;
    --grey-rule:#8b8b8b;
    --wood:#8a5a2b;
  }
  *{margin:0;padding:0;box-sizing:border-box}
  html,body{width:903px;height:1200px;overflow:hidden;background:var(--sheet)}
  .canvas{position:relative;width:903px;height:1200px;background:var(--sheet)}
  .stage{position:absolute;left:0;top:417px;width:903px;height:783px;background:var(--stage)}
  .card{position:absolute;width:387px;height:235px;display:block}
  .card--night-gold{left:26px;top:97px}
  .card--night-blue{left:472px;top:93px}
  .card--windmill{left:26px;top:501px}
  .card--wheat-corner{left:472px;top:501px}
  .card--haze-light{left:26px;top:917px}
  .card--haze-warm{left:472px;top:917px}
  .name-sans{font-family:"Fira Sans",sans-serif;font-weight:400;font-size:15px}
  .name-slab{font-family:"Alfa Slab One",serif;font-size:14px}
  .contact{font-family:"Fira Sans",sans-serif;font-weight:600;font-size:6.8px}
  .contact-slab{font-family:"Alfa Slab One",serif;font-size:6.4px}
  .address{font-family:"Fira Sans",sans-serif;font-weight:400;font-size:7.4px}
  .address-slab{font-family:"Alfa Slab One",serif;font-size:7px}
</style>
</head>
<body>
<main class="canvas">
  <div class="stage"></div>

  <!-- Concept 1: night blue with golden wheat -->
  <svg class="card card--night-gold" viewBox="0 0 255 155" role="group" aria-label="Business card, night blue with gold wheat">
    <defs>
      <radialGradient id="nightGoldBg" cx="0.15" cy="0.9" r="0.95">
        <stop offset="0" stop-color="var(--ocean)"/><stop offset="0.55" stop-color="#08397a"/><stop offset="1" stop-color="var(--night)"/>
      </radialGradient>
      <linearGradient id="wheatGold" x1="0" y1="0" x2="1" y2="1">
        <stop offset="0" stop-color="var(--gold-soft)" stop-opacity="0.85"/><stop offset="1" stop-color="var(--gold)" stop-opacity="0.9"/>
      </linearGradient>
    </defs>
    <rect width="255" height="155" fill="url(#nightGoldBg)"/>
    <path role="img" aria-label="Illustration of golden wheat stalks" d="M125 0 H228 V150 C215 120 200 80 170 40 C155 20 140 8 125 0Z" fill="url(#wheatGold)"/>
    <line x1="0" y1="47" x2="250" y2="47" stroke="var(--teal-rule)" stroke-width="0.8"/>
    <line x1="230" y1="0" x2="230" y2="155" stroke="var(--teal-rule)" stroke-width="0.6"/>
    <rect x="207" y="24" width="36" height="23" fill="none" stroke="var(--teal-rule)" stroke-width="0.6"/>
    <line x1="28" y1="130" x2="190" y2="130" stroke="var(--teal-rule)" stroke-width="0.6"/>
    <line x1="33" y1="108" x2="33" y2="155" stroke="var(--teal-rule)" stroke-width="0.6"/>
    <text class="name-sans" x="14" y="36" fill="var(--yellow-ink)">Tess Marlowe</text>
    <text class="contact" x="37" y="115" fill="var(--yellow-ink)">M: 0427 391 864</text>
    <text class="contact" x="37" y="126" fill="var(--yellow-ink)">E: tess@tmcommsmail.com</text>
    <g transform="translate(239 151) rotate(-90)">
      <text class="address" x="0" y="0" fill="var(--yellow-ink)">PO Box 152</text>
      <text class="address" x="0" y="10" fill="var(--yellow-ink)">Durrandale Q 4472</text>
    </g>
  </svg>

  <!-- Concept 2: indigo with blue wheat -->
  <svg class="card card--night-blue" viewBox="0 0 255 155" role="group" aria-label="Business card, indigo with blue wheat">
    <defs>
      <radialGradient id="nightBlueBg" cx="0.2" cy="0.85" r="0.95">
        <stop offset="0" stop-color="#1530c8"/><stop offset="0.55" stop-color="var(--indigo)"/><stop offset="1" stop-color="var(--night)"/>
      </radialGradient>
      <linearGradient id="wheatBlue" x1="0" y1="0" x2="1" y2="1">
        <stop offset="0" stop-color="#6fa2ff" stop-opacity="0.85"/><stop offset="1" stop-color="var(--sky-blue)" stop-opacity="0.9"/>
      </linearGradient>
    </defs>
    <rect width="255" height="155" fill="url(#nightBlueBg)"/>
    <path role="img" aria-label="Illustration of blue wheat stalks" d="M125 0 H228 V150 C215 120 200 80 170 40 C155 20 140 8 125 0Z" fill="url(#wheatBlue)"/>
    <line x1="0" y1="45" x2="250" y2="45" stroke="var(--teal-rule)" stroke-width="0.8"/>
    <line x1="230" y1="0" x2="230" y2="155" stroke="var(--teal-rule)" stroke-width="0.6"/>
    <rect x="207" y="23" width="36" height="22" fill="none" stroke="var(--teal-rule)" stroke-width="0.6"/>
    <line x1="28" y1="132" x2="190" y2="132" stroke="var(--teal-rule)" stroke-width="0.6"/>
    <line x1="31" y1="108" x2="31" y2="155" stroke="var(--teal-rule)" stroke-width="0.6"/>
    <text class="name-sans" x="14" y="35" fill="var(--cyan-ink)">Tess Marlowe</text>
    <text class="contact" x="35" y="117" fill="var(--cyan-ink)">M: 0427 391 864</text>
    <text class="contact" x="35" y="128" fill="var(--cyan-ink)">E: tess@tmcommsmail.com</text>
    <g transform="translate(238 151) rotate(-90)">
      <text class="address" x="0" y="0" fill="var(--cyan-ink)">PO Box 152</text>
      <text class="address" x="0" y="10" fill="var(--cyan-ink)">Durrandale Q 4472</text>
    </g>
  </svg>

  <!-- Concept 3: white with windmill -->
  <svg class="card card--windmill" viewBox="0 0 255 155" role="group" aria-label="Business card, white with wheat and windmill">
    <defs>
      <linearGradient id="wheatGoldLight" x1="0" y1="0" x2="1" y2="1">
        <stop offset="0" stop-color="var(--gold-soft)" stop-opacity="0.75"/><stop offset="1" stop-color="var(--gold)" stop-opacity="0.85"/>
      </linearGradient>
      <linearGradient id="windmillTone" x1="0" y1="0" x2="0" y2="1">
        <stop offset="0" stop-color="#d9b98a"/><stop offset="1" stop-color="var(--wood)"/>
      </linearGradient>
    </defs>
    <rect width="255" height="155" fill="var(--sheet)"/>
    <path role="img" aria-label="Illustration of golden wheat stalks" d="M125 0 H228 V150 C215 120 200 80 170 40 C155 20 140 8 125 0Z" fill="url(#wheatGoldLight)"/>
    <rect role="img" aria-label="Illustration of a wooden windmill" x="0" y="58" width="74" height="97" fill="url(#windmillTone)" opacity="0.85"/>
    <line x1="0" y1="43" x2="255" y2="43" stroke="var(--red-rule)" stroke-width="0.8"/>
    <line x1="222" y1="0" x2="222" y2="155" stroke="var(--grey-rule)" stroke-width="0.6"/>
    <rect x="214" y="24" width="31" height="34" fill="none" stroke="var(--red-rule)" stroke-width="0.6"/>
    <line x1="0" y1="131" x2="195" y2="131" stroke="var(--red-rule)" stroke-width="0.6"/>
    <text class="name-slab" x="14" y="35" fill="var(--red-ink)">Tess Marlowe</text>
    <text class="contact-slab" x="70" y="117" fill="var(--red-ink)">M: 0427 391 864</text>
    <text class="contact-slab" x="70" y="128" fill="var(--red-ink)">E: tess@tmcommsmail.com</text>
    <g transform="translate(236 152) rotate(-90)">
      <text class="address-slab" x="0" y="0" fill="var(--red-ink)">PO Box 152</text>
      <text class="address-slab" x="0" y="10" fill="var(--red-ink)">Durrandale Q 4472</text>
    </g>
  </svg>

  <!-- Concept 4: white with corner wheat -->
  <svg class="card card--wheat-corner" viewBox="0 0 255 155" role="group" aria-label="Business card, white with wheat accents">
    <defs>
      <linearGradient id="wheatGoldLight2" x1="0" y1="0" x2="1" y2="1">
        <stop offset="0" stop-color="var(--gold-soft)" stop-opacity="0.75"/><stop offset="1" stop-color="var(--gold)" stop-opacity="0.85"/>
      </linearGradient>
    </defs>
    <rect width="255" height="155" fill="var(--sheet)"/>
    <path role="img" aria-label="Illustration of golden wheat stalks" d="M125 0 H228 V150 C215 120 200 80 170 40 C155 20 140 8 125 0Z" fill="url(#wheatGoldLight2)"/>
    <path role="img" aria-label="Illustration of small wheat heads" d="M0 155 V112 C20 100 45 98 62 104 C40 118 20 135 12 155Z" fill="url(#wheatGoldLight2)"/>
    <line x1="0" y1="43" x2="255" y2="43" stroke="var(--red-rule)" stroke-width="0.8"/>
    <line x1="222" y1="0" x2="222" y2="155" stroke="var(--grey-rule)" stroke-width="0.6"/>
    <rect x="214" y="24" width="31" height="34" fill="none" stroke="var(--red-rule)" stroke-width="0.6"/>
    <line x1="0" y1="131" x2="190" y2="131" stroke="var(--red-rule)" stroke-width="0.6"/>
    <line x1="30" y1="105" x2="30" y2="155" stroke="var(--grey-rule)" stroke-width="0.6"/>
    <text class="name-slab" x="14" y="35" fill="var(--red-ink)">Tess Marlowe</text>
    <text class="contact-slab" x="70" y="117" fill="var(--red-ink)">M: 0427 391 864</text>
    <text class="contact-slab" x="70" y="128" fill="var(--red-ink)">E: tess@tmcommsmail.com</text>
    <g transform="translate(236 152) rotate(-90)">
      <text class="address-slab" x="0" y="0" fill="var(--red-ink)">PO Box 152</text>
      <text class="address-slab" x="0" y="10" fill="var(--red-ink)">Durrandale Q 4472</text>
    </g>
  </svg>

  <!-- Concept 5: white with light golden haze -->
  <svg class="card card--haze-light" viewBox="0 0 255 155" role="group" aria-label="Business card, white with soft gold haze">
    <defs>
      <radialGradient id="hazeLight" cx="0.1" cy="0.95" r="0.65">
        <stop offset="0" stop-color="var(--gold-soft)" stop-opacity="0.95"/><stop offset="1" stop-color="var(--gold-soft)" stop-opacity="0"/>
      </radialGradient>
      <linearGradient id="wheatGoldLight3" x1="0" y1="0" x2="1" y2="1">
        <stop offset="0" stop-color="var(--gold-soft)" stop-opacity="0.75"/><stop offset="1" stop-color="var(--gold)" stop-opacity="0.85"/>
      </linearGradient>
    </defs>
    <rect width="255" height="155" fill="var(--sheet)"/>
    <rect width="255" height="155" fill="url(#hazeLight)"/>
    <path role="img" aria-label="Illustration of golden wheat stalks" d="M125 0 H228 V150 C215 120 200 80 170 40 C155 20 140 8 125 0Z" fill="url(#wheatGoldLight3)"/>
    <line x1="0" y1="43" x2="255" y2="43" stroke="var(--red-rule)" stroke-width="0.8"/>
    <line x1="222" y1="0" x2="222" y2="155" stroke="var(--grey-rule)" stroke-width="0.6"/>
    <rect x="214" y="24" width="31" height="34" fill="none" stroke="var(--red-rule)" stroke-width="0.6"/>
    <line x1="26" y1="131" x2="190" y2="131" stroke="var(--red-rule)" stroke-width="0.6"/>
    <line x1="32" y1="105" x2="32" y2="155" stroke="var(--red-rule)" stroke-width="0.6"/>
    <text class="name-sans" x="14" y="35" fill="var(--red-ink)">Tess Marlowe</text>
    <text class="contact" x="36" y="117" fill="var(--red-ink)">M: 0427 391 864</text>
    <text class="contact" x="36" y="128" fill="var(--red-ink)">E: tess@tmcommsmail.com</text>
    <g transform="translate(236 152) rotate(-90)">
      <text class="address" x="0" y="0" fill="var(--red-ink)">PO Box 152</text>
      <text class="address" x="0" y="10" fill="var(--red-ink)">Durrandale Q 4472</text>
    </g>
  </svg>

  <!-- Concept 6: white with warm golden haze -->
  <svg class="card card--haze-warm" viewBox="0 0 255 155" role="group" aria-label="Business card, white with warm gold haze">
    <defs>
      <radialGradient id="hazeWarm" cx="0.35" cy="0.85" r="0.7">
        <stop offset="0" stop-color="var(--gold-soft)" stop-opacity="1"/><stop offset="0.6" stop-color="var(--gold-soft)" stop-opacity="0.7"/><stop offset="1" stop-color="var(--gold-soft)" stop-opacity="0"/>
      </radialGradient>
      <linearGradient id="wheatGoldLight4" x1="0" y1="0" x2="1" y2="1">
        <stop offset="0" stop-color="var(--gold-soft)" stop-opacity="0.75"/><stop offset="1" stop-color="var(--gold)" stop-opacity="0.85"/>
      </linearGradient>
    </defs>
    <rect width="255" height="155" fill="var(--sheet)"/>
    <rect width="255" height="155" fill="url(#hazeWarm)"/>
    <path role="img" aria-label="Illustration of golden wheat stalks" d="M125 0 H228 V150 C215 120 200 80 170 40 C155 20 140 8 125 0Z" fill="url(#wheatGoldLight4)"/>
    <line x1="0" y1="43" x2="255" y2="43" stroke="var(--red-rule)" stroke-width="0.8"/>
    <line x1="222" y1="0" x2="222" y2="155" stroke="var(--grey-rule)" stroke-width="0.6"/>
    <rect x="214" y="24" width="31" height="34" fill="none" stroke="var(--red-rule)" stroke-width="0.6"/>
    <line x1="26" y1="131" x2="190" y2="131" stroke="var(--red-rule)" stroke-width="0.6"/>
    <line x1="32" y1="105" x2="32" y2="155" stroke="var(--red-rule)" stroke-width="0.6"/>
    <text class="name-sans" x="14" y="35" fill="var(--red-ink)">Tess Marlowe</text>
    <text class="contact" x="36" y="117" fill="var(--red-ink)">M: 0427 391 864</text>
    <text class="contact" x="36" y="128" fill="var(--red-ink)">E: tess@tmcommsmail.com</text>
    <g transform="translate(236 152) rotate(-90)">
      <text class="address" x="0" y="0" fill="var(--red-ink)">PO Box 152</text>
      <text class="address" x="0" y="10" fill="var(--red-ink)">Durrandale Q 4472</text>
    </g>
  </svg>
</main>
</body>
</html>
```